Oil and Gas Company: Letterhead Design

In short we need a professional company letterhead designed for our Oil and Gas company.

We would like to keep the design simple and professional. Letterhead to include the company logo and color scheme, front page and continuation pages.

For reference, see attached logo below with our company logo and color scheme.

Target Market(s)

Oil & Gas Market

Industry/Entity Type

Oil And Gas

Font styles to use
Sans Serif

Requirements
Must have
• Letterhead must contain a front page & continuation page.
• Must be simple and professional in design.
• Follow our logo and color scheme.
Nice to have
• I would like to have the logo embedded in the bottom right hand portion of the page to provide some depth into the letterhead.

```html
<!DOCTYPE html>
<html lang="en">
<head>
<meta charset="utf-8">
<title>Ridgeline Energy Services – Stationery</title>
<link href="https://fonts.googleapis.com/css2?family=Roboto:wght@400;500&display=swap" rel="stylesheet">
<style>
  :root {
    --backdrop: #d4d4d4;
    --brand-red: #d41f26;
    --paper: #f0f0f0;
    --ink: #5a5a5a;
    --ink-dark: #2b2b2b;
    --white: #ffffff;
    --watermark: rgba(255, 255, 255, 0.13);
  }
  html, body {
    margin: 0;
    padding: 0;
    width: 1200px;
    height: 810px;
    overflow: hidden;
    background: var(--backdrop);
    font-family: "Roboto", Arial, sans-serif;
  }
  .stationery {
    position: relative;
    width: 1200px;
    height: 810px;
  }
  .sheet {
    position: absolute;
    overflow: hidden;
  }
  .sheet--cover {
    left: 121px;
    top: 112px;
    width: 436px;
    height: 614px;
    background: var(--brand-red);
  }
  .sheet--letter {
    left: 654px;
    top: 111px;
    width: 436px;
    height: 616px;
    background: var(--paper);
  }

  /* Cover page */
  .cover-watermark {
    position: absolute;
    left: 10px;
    top: -20px;
    width: 380px;
    height: 380px;
    border-radius: 50%;
    background: var(--watermark);
  }
  .cover-mark {
    position: absolute;
    left: 283px;
    top: 452px;
    width: 68px;
    height: 68px;
    border-radius: 50%;
    background: var(--white);
  }
  .cover-brand {
    position: absolute;
    left: 227px;
    top: 539px;
    width: 180px;
    margin: 0;
    text-align: center;
    color: var(--white);
    font-size: 15.5px;
    font-weight: 400;
    letter-spacing: 0.6px;
    line-height: 16px;
  }

  /* Letter page */
  .letter-mark {
    position: absolute;
    left: 64px;
    top: 32px;
    width: 48px;
    height: 48px;
    border-radius: 50%;
    background: var(--brand-red);
  }
  .letter-brand {
    position: absolute;
    left: 33px;
    top: 92px;
    width: 110px;
    margin: 0;
    text-align: center;
    color: var(--ink-dark);
    font-size: 10.4px;
    font-weight: 500;
    line-height: 11px;
    letter-spacing: 0.3px;
  }
  .contact {
    position: absolute;
    left: 302px;
    top: 58px;
    margin: 0;
    color: var(--ink);
    font-size: 6.6px;
    line-height: 9.8px;
    font-style: normal;
  }
  .contact__address { margin-bottom: 5px; }
  .contact__line {
    display: flex;
    align-items: center;
    gap: 3px;
  }
  .contact__icon { width: 7px; height: 7px; }
  .recipient {
    position: absolute;
    left: 38px;
    top: 184px;
    margin: 0;
    color: var(--ink);
    font-size: 7.4px;
    line-height: 11.5px;
  }
  .letter-body {
    position: absolute;
    left: 38px;
    top: 253px;
    width: 362px;
    color: var(--ink);
    font-size: 7.2px;
    line-height: 11.4px;
    text-align: justify;
  }
  .letter-body p { margin: 0 0 22px; }
  .signature {
    position: absolute;
    left: 38px;
    top: 417px;
    width: 82px;
    height: 54px;
    border-radius: 3px;
    background: linear-gradient(135deg, rgba(212,31,38,0.18), rgba(212,31,38,0.06));
  }
  .signatory {
    position: absolute;
    left: 38px;
    top: 482px;
    margin: 0;
    color: var(--ink);
    font-size: 7.4px;
  }
</style>
</head>
<body>
<main class="stationery">
  <section class="sheet sheet--cover" aria-label="Letterhead cover page">
    <div class="cover-watermark" aria-hidden="true"></div>
    <div class="cover-mark" aria-hidden="true"></div>
    <p class="cover-brand">RIDGELINE<br>ENERGY SERVICES</p>
  </section>

  <section class="sheet sheet--letter" aria-label="Letterhead front page">
    <div class="letter-mark" aria-hidden="true"></div>
    <p class="letter-brand">RIDGELINE<br>ENERGY SERVICES</p>

    <address class="contact">
      <div class="contact__address">Suite 5, 120 Harbour Road<br>Eastport, VIC 3100</div>
      <div class="contact__line">
        <svg class="contact__icon" viewBox="0 0 10 10" aria-hidden="true"><path d="M2 1 L4 1 L4.5 3 L3.3 4 Q4.5 6 6 6.7 L7 5.5 L9 6 L9 8 Q5 9 2.5 6 Q0.5 3.5 2 1Z" fill="#d41f26"/></svg>
        <span>800-555-0147</span>
      </div>
      <div class="contact__line">
        <svg class="contact__icon" viewBox="0 0 10 10" aria-hidden="true"><rect x="0.5" y="2" width="9" height="6" fill="#d41f26"/><path d="M0.5 2 L5 5.5 L9.5 2" stroke="#fff" stroke-width="0.9" fill="none"/></svg>
        <span>hello@ridgelineenergy.com</span>
      </div>
      <div class="contact__line">
        <svg class="contact__icon" viewBox="0 0 10 10" aria-hidden="true"><circle cx="5" cy="5" r="4.3" fill="#d41f26"/><path d="M0.7 5 H9.3 M5 0.7 Q2.5 5 5 9.3 M5 0.7 Q7.5 5 5 9.3" stroke="#fff" stroke-width="0.7" fill="none"/></svg>
        <span>www.ridgelineenergy.com</span>
      </div>
    </address>

    <p class="recipient">Dear Whitlock<br>KTL Design Works Company<br>Department Design</p>

    <div class="letter-body">
      <p>Lorem ipsum dolor sit amet, consectetuer adipiscing elit. Aenean commodo ligula eget dolor. Aenean massa. Cum sociis natoque penatibus et magnis dis parturient montes, nascetur ridiculus mus. Donec quam felis, ultricies nec, pellentesque eu, pretium quis, sem. Nulla consequat massa quis enim. Donec pede justo, fringilla vel, aliquet nec, vulputate eget, arcu. In enim justo, rhoncus ut, imperdiet a, venenatis vitae, justo. Nullam dictum felis eu pede mollis pretium. Integer tincidunt. Cras dapibus. Vivamus elementum semper nisi.Nullam dictum felis eu pede mollis pretium. Integer tincidunt. Cras dapibus. Vivamus elementum semper nisi.felis eu pede mollis pretium. Integer tincidunt. Cras dapibus.</p>
      <p>Quisque rutrum. Aenean imperdiet. Etiam ultricies nisi vel augue. Curabitur ullamcorper ultricies nisi. Nam eget dui. Etiam rhoncus. Maecenas tempus, tellus eget condimentum rhoncus, sem quam semper libero, sit amet adipiscing sem neque sed ipsum.felis pede mollis pretium. I am tincidunt. Cras dapibus.</p>
    </div>

    <div class="signature" role="img" aria-label="Handwritten signature of the director in red ink"></div>
    <p class="signatory">Director/Excecutive Director</p>
  </section>
</main>
</body>
</html>
```